Commercial cleaning business needs a trifold brochure to spotlight janitorial services offered.

Looking for a catchy, creative, trifold brochure to give a description of services offered. This would be used for new potential customers. Our primary colors are royal blue, light gray, and white as included in our logo. The logo does include "restoration", however we only want this brochure to be focused solely on the commercial cleaning side for janitorial services as we already purchased a brochure for the restoration. You can visit our website to get a better idea. www.vtlqservices.example

```html
<!DOCTYPE html>
<html lang="en">
<head>
<meta charset="utf-8">
<title>VTLQ Commercial Cleaning – Trifold Brochure</title>
<link href="https://fonts.googleapis.com/css2?family=Oswald:wght@500&family=Open+Sans:wght@400;600&display=swap" rel="stylesheet">
<style>
:root{
  --royal:#2f2b86;
  --royal-deep:#24206e;
  --royal-light:#4a46a6;
  --gray:#d9d9de;
  --gray-mid:#a9a9b2;
  --paper:#f1f1f4;
  --white:#ffffff;
  --ink:#4a4a55;
  --backdrop:#e4e4e7;
}
*{box-sizing:border-box;margin:0;padding:0}
html,body{width:1200px;height:900px;overflow:hidden;background:var(--backdrop)}
body{position:relative;font-family:"Open Sans",sans-serif;color:var(--ink)}
.spread{position:absolute;left:295px;width:610px;height:430px;display:flex;box-shadow:0 4px 14px rgba(0,0,0,.18);background:var(--paper)}
.spread--outside{top:15px}
.spread--inside{top:455px}
.panel{position:relative;width:203.33px;height:100%;overflow:hidden}
.photo{position:absolute;left:0;width:100%}
.swoosh{position:absolute;left:0;width:100%;height:100%;top:0;pointer-events:none}
.heading{font-family:"Oswald",sans-serif;font-weight:500;color:var(--royal);text-transform:uppercase;line-height:1.15;letter-spacing:.2px}
.body-text{font-size:7.4px;line-height:1.45;text-align:justify}
.body-text--compact{font-size:6.9px;line-height:1.4}
.abs{position:absolute}
.brand{display:flex;align-items:center;justify-content:center;gap:6px}
.brand__dot{width:14px;height:14px;border-radius:50%;background:var(--royal)}
.brand__name{font-family:"Open Sans",sans-serif;font-weight:600;color:var(--royal);font-size:24px;letter-spacing:1px}
.brand__tag{font-size:7px;font-weight:600;color:var(--royal);text-align:center;margin-top:2px}
.phone-pill{display:flex;align-items:center;justify-content:center;gap:6px;background:var(--gray);border-radius:12px;height:22px;font-family:"Oswald",sans-serif;font-weight:500;color:var(--royal);font-size:15px}
.phone-pill svg{width:11px;height:11px}
.white{color:var(--white)}
.center{text-align:center}
.bullets{list-style:none}
.bullets li{position:relative;padding-left:14px;margin-bottom:12px;font-size:7.6px;line-height:1.45;color:var(--white)}
.bullets li::before{content:"";position:absolute;left:0;top:2px;width:8px;height:8px;border-radius:50%;background:var(--white)}
.bullets li::after{content:"";position:absolute;left:2px;top:4.2px;border-left:4px solid var(--royal);border-top:2px solid transparent;border-bottom:2px solid transparent;margin-left:1px}
.service-grid{display:flex;flex-wrap:wrap;justify-content:center;gap:8px 14px}
.service{width:52px;text-align:center;font-size:5.8px;line-height:1.3;color:var(--ink)}
.service__icon{width:38px;height:38px;border-radius:50%;background:var(--royal);margin:0 auto 3px;border:2px solid var(--gray)}
.social{display:flex;justify-content:center;gap:8px}
.social span{width:11px;height:11px;border-radius:50%;border:1px solid var(--white)}
</style>
</head>
<body>

<section class="spread spread--outside" aria-label="Brochure outside">

  <div class="panel">
    <div class="photo" style="top:0;height:175px;background:linear-gradient(160deg,#c9c3b8,#8f8c91 55%,#5d5a70)" role="img" aria-label="Photo of a worker polishing an office floor with a floor machine"></div>
    <svg class="swoosh" viewBox="0 0 203 430" preserveAspectRatio="none">
      <path d="M0 165 Q90 140 203 110 L203 430 L0 430Z" fill="var(--royal)"/>
      <path d="M0 172 Q95 148 203 122 L203 430 L0 430Z" fill="var(--gray-mid)"/>
      <path d="M0 178 Q100 156 203 130 L203 430 L0 430Z" fill="var(--paper)"/>
      <path d="M0 380 Q100 364 203 345 L203 430 L0 430Z" fill="var(--royal)"/>
      <path d="M0 375 Q100 359 203 340" stroke="var(--gray-mid)" stroke-width="2" fill="none"/>
    </svg>
    <h2 class="heading abs" style="left:12px;top:184px;font-size:13px">Experience<br>High-Tech Efficiency</h2>
    <p class="body-text body-text--compact abs" style="left:12px;top:217px;width:180px">Vantage Tri-Line Building Maintenance follows a technology-based service delivery process. In our company, employees communicate with each other using smartphone/tablet apps so that they can track every cleaning team's whereabouts.</p>
    <p class="body-text body-text--compact abs" style="left:12px;top:268px;width:180px">This enables main office managers to efficiently monitor work progress in real time. With this high-tech infrastructure in place, our cleaners can be able to relay on-the-spot customer requests to us immediately. We can then issue instructions just as quickly to employees on site.</p>
    <p class="abs white center" style="left:10px;top:393px;width:183px;font-size:7.6px;line-height:1.5;letter-spacing:.3px">It's not just about cleaning,<br>it's about the communication.</p>
  </div>

  <div class="panel">
    <svg class="swoosh" viewBox="0 0 203 430" preserveAspectRatio="none">
      <path d="M0 0 H203 V95 Q100 105 0 135Z" fill="var(--royal)"/>
      <path d="M0 135 Q100 105 203 95 V102 Q100 112 0 142Z" fill="var(--gray-mid)"/>
      <path d="M0 345 Q100 330 203 312 V430 H0Z" fill="var(--royal)"/>
      <path d="M0 340 Q100 325 203 307" stroke="var(--gray-mid)" stroke-width="2" fill="none"/>
    </svg>
    <div class="abs" style="left:56px;top:15px;width:92px;height:92px;border-radius:50%;border:3px solid var(--white);background:linear-gradient(160deg,#c8ccd6,#6d86a8 60%,#3e4f7a)" role="img" aria-label="Circular photo of a cleaner mopping a hallway"></div>
    <h2 class="heading abs center" style="left:0;width:100%;top:128px;font-size:13px">Contact Us</h2>
    <p class="abs center" style="left:14px;width:175px;top:150px;font-size:7.4px;line-height:1.4">Get in touch with us to order janitorial supplies for your offices. You may speak to any of our sales staff to inquire about the range of products we have and their corresponding prices.</p>
    <p class="abs center" style="left:14px;width:175px;top:212px;font-size:7.4px;line-height:1.4">We serve clients all throughout Central and Eastern Kentucky.</p>
    <div class="abs" style="left:0;width:100%;top:250px">
      <div class="brand"><span class="brand__dot"></span><span class="brand__name" style="font-size:18px">VTLQ</span></div>
      <div class="brand__tag" style="font-size:5.5px">Commercial Cleaning &amp; Restoration</div>
    </div>
    <div class="social abs" style="left:0;width:100%;top:338px"><span></span><span></span><span></span></div>
    <h2 class="heading abs center white" style="left:0;width:100%;top:355px;font-size:13px">Free Quote or Estimate!</h2>
    <p class="abs center white" style="left:0;width:100%;top:378px;font-size:7.4px;line-height:1.75;letter-spacing:.3px">1-800-555-0142<br>sales@vtlqservices.example<br>www.vtlqservices.example</p>
  </div>

  <div class="panel">
    <svg class="swoosh" viewBox="0 0 203 430" preserveAspectRatio="none">
      <path d="M0 0 H203 V95 H0Z" fill="var(--gray)"/>
      <path d="M0 312 Q100 300 203 295 V430 H0Z" fill="var(--royal)"/>
    </svg>
    <div class="abs" style="left:0;width:100%;top:26px">
      <div class="brand"><span class="brand__dot"></span><span class="brand__name">VTLQ</span></div>
      <div class="brand__tag">Commercial Cleaning &amp; Restoration</div>
    </div>
    <div class="photo" style="top:98px;height:195px;background:linear-gradient(170deg,#d6d6da,#8d9bb4 50%,#3d5489)" role="img" aria-label="Photo of smiling cleaning staff in blue uniforms wiping office desks"></div>
    <svg class="swoosh" viewBox="0 0 203 430" preserveAspectRatio="none">
      <path d="M0 298 Q100 286 203 281 V292 Q100 297 0 312Z" fill="var(--gray-mid)"/>
      <path d="M0 304 Q100 292 203 287 V300 Q100 304 0 318Z" fill="var(--royal)"/>
    </svg>
    <h1 class="heading abs center white" style="left:0;width:100%;top:318px;font-size:17px">Commercial Cleaning</h1>
    <p class="abs center" style="left:0;width:100%;top:343px;font-size:7.6px;color:var(--gray)">Experience High-Tech Efficiency</p>
    <div class="phone-pill abs" style="left:18px;width:167px;top:363px">
      <svg viewBox="0 0 12 12"><path d="M3 1h2l1 3-1.5 1a6 6 0 0 0 2.5 2.5L8 6l3 1v2a1.5 1.5 0 0 1-1.5 1.5A8.5 8.5 0 0 1 1.5 2.5 1.5 1.5 0 0 1 3 1z" fill="var(--royal)"/></svg>1-800-555-0142</div>
    <p class="abs center white" style="left:0;width:100%;top:397px;font-size:7.6px;letter-spacing:.4px">www.vtlqservices.example</p>
  </div>
</section>

<section class="spread spread--inside" aria-label="Brochure inside">

  <div class="panel">
    <div class="photo" style="top:0;height:185px;background:linear-gradient(165deg,#b8a48c,#7b6a5a 45%,#3b3a44)" role="img" aria-label="Photo of a cleaner wiping a conference table with microphones"></div>
    <svg class="swoosh" viewBox="0 0 203 430" preserveAspectRatio="none">
      <path d="M0 178 Q100 160 203 168 V430 H0Z" fill="var(--gray-mid)"/>
      <path d="M0 186 Q100 168 203 176 V430 H0Z" fill="var(--gray)"/>
      <path d="M0 200 Q100 178 203 186 V430 H0Z" fill="var(--royal)"/>
    </svg>
    <h2 class="heading abs white" style="left:12px;top:208px;font-size:13px">About Us</h2>
    <p class="body-text abs white" style="left:12px;top:234px;width:180px">Vantage Tri-Line Building Maintenance is committed to providing an unsurpassed level of janitorial services and building long-lasting relationships with clients. We accomplish this by using modern technology to communicate effectively with client's and employees.</p>
    <p class="body-text abs white" style="left:12px;top:318px;width:180px">Our team leaders assist clients in defining their needs and communicate those needs to our employees. We act with integrity in all aspects of our business at all times. Our goal is to deliver a consistently high level of janitorial services that are within your budget.</p>
  </div>

  <div class="panel" style="background:var(--paper)">
    <div class="abs" style="left:0;width:100%;top:28px">
      <div class="brand"><span class="brand__dot"></span><span class="brand__name" style="font-size:20px">VTLQ</span></div>
      <div class="brand__tag" style="font-size:6px">Commercial Cleaning &amp; Restoration</div>
    </div>
    <h2 class="heading abs center" style="left:0;width:100%;top:95px;font-size:13px">Our Services</h2>
    <p class="abs" style="left:12px;width:180px;top:117px;font-size:7.4px;line-height:1.4">Our company specializes in cleaning medical facilities and class-A office spaces. You can contact us to request:</p>
    <div class="service-grid abs" style="left:6px;width:191px;top:172px">
      <div class="service"><div class="service__icon" role="img" aria-label="Carpet cleaning icon"></div>Carpet Cleaning</div>
      <div class="service"><div class="service__icon" role="img" aria-label="Floor care icon"></div>Floor Care</div>
      <div class="service"><div class="service__icon" role="img" aria-label="Janitorial services icon"></div>Janitorial Services</div>
      <div class="service"><div class="service__icon" role="img" aria-label="Window cleaning icon"></div>Window Cleaning</div>
      <div class="service" style="width:80px"><div class="service__icon" role="img" aria-label="24-hour emergency icon"></div>24- Hour Emergency Water Extraction Services</div>
    </div>
    <div class="abs" style="left:10px;top:313px;display:flex;gap:2px">
      <div style="width:60px;height:60px;border-radius:50%;background:linear-gradient(150deg,#d8d8dc,#8f949e)" role="img" aria-label="Photo of vacuuming a carpet"></div>
      <div style="width:60px;height:60px;border-radius:50%;background:linear-gradient(150deg,#c9a57c,#5f6fa3)" role="img" aria-label="Photo of a smiling cleaner with supplies"></div>
      <div style="width:60px;height:60px;border-radius:50%;background:linear-gradient(150deg,#e0e0e3,#9a9aa3)" role="img" aria-label="Photo of a floor scrubbing machine"></div>
    </div>
    <div class="phone-pill abs" style="left:10px;width:183px;top:387px;background:var(--royal);color:var(--white);height:26px;font-size:16px">
      <svg viewBox="0 0 12 12"><path d="M3 1h2l1 3-1.5 1a6 6 0 0 0 2.5 2.5L8 6l3 1v2a1.5 1.5 0 0 1-1.5 1.5A8.5 8.5 0 0 1 1.5 2.5 1.5 1.5 0 0 1 3 1z" fill="var(--white)"/></svg>1-800-555-0142</div>
  </div>

  <div class="panel" style="background:var(--royal)">
    <div class="photo" style="top:275px;height:155px;background:linear-gradient(170deg,#e6e3dc,#b9b0a0 50%,#7b7a8c)" role="img" aria-label="Photo of a janitor mopping beside a wet floor sign"></div>
    <svg class="swoosh" viewBox="0 0 203 430" preserveAspectRatio="none">
      <path d="M0 250 Q100 285 203 262 V0 H0Z" fill="var(--royal)"/>
      <path d="M0 250 Q100 285 203 262" stroke="var(--white)" stroke-width="6" fill="none"/>
      <path d="M0 258 Q100 293 203 270" stroke="var(--gray-mid)" stroke-width="3" fill="none"/>
    </svg>
    <h2 class="heading abs white" style="left:12px;top:30px;font-size:13px">We Inspect Our Work</h2>
    <ul class="bullets abs" style="left:12px;width:180px;top:60px">
      <li>We focus on our cleaners so that they can focus on you. Finding the perfect cleaner can be a real challenge.</li>
      <li>It's not just about cleaning, it's about communication. VTLQ recognizes that doing a great job is more than just providing great cleaning.</li>
      <li>No cleaning company cares more about quality, and we can prove it. From the technology we use, to our quality inspections, we invest heavily in making sure that we are providing you the best possible cleaning services.</li>
    </ul>
  </div>
</section>

</body>
</html>
```